" A empresa está localizada numa cidade pequena, porém muito próximos da capital do estado de Minas Gerais e de outras cidades maiores do interior. Considerada região metropolitana da capital. Criaremos um site e faremos venda de produtos na loja virtual, bem como marcação de serviços. Queremos trazer profissionalismo e um serviço diferenciado para a região. Nossa meta é em 3 anos ser a principal referência nesse serviço num raio de 50 km da cidade. "

```html
<!DOCTYPE html>
<html lang="pt-BR">
<head>
<meta charset="UTF-8">
<title>Folha Clara — Adesivo</title>
<link href="https://fonts.googleapis.com/css2?family=Cinzel:wght@400;500&family=Cormorant+Garamond:wght@500&family=Montserrat:wght@500&display=swap" rel="stylesheet">
<style>
  :root {
    --page-bg: #ececec;
    --sticker-teal: #1f4749;
    --sticker-teal-deep: #173a3c;
    --gold: #c9a866;
    --gold-light: #e2c98f;
  }
  * { margin: 0; padding: 0; box-sizing: border-box; }
  html, body {
    width: 1200px;
    height: 1200px;
    overflow: hidden;
    background: var(--page-bg);
  }
  .canvas {
    position: relative;
    width: 1200px;
    height: 1200px;
    display: flex;
    align-items: center;
    justify-content: center;
  }
  .sticker {
    position: relative;
    width: 1000px;
    height: 1000px;
    border-radius: 50%;
    background: radial-gradient(circle at 50% 40%, var(--sticker-teal) 0%, var(--sticker-teal-deep) 100%);
  }
  .sticker__ring {
    position: absolute;
    inset: 38px;
    border-radius: 50%;
    border: 6px solid var(--gold);
  }
  .brand {
    position: absolute;
    left: 0;
    right: 0;
    top: 150px;
    display: flex;
    flex-direction: column;
    align-items: center;
  }
  .brand__dot {
    width: 150px;
    height: 150px;
    border-radius: 50%;
    border: 6px solid var(--gold);
    margin-bottom: 60px;
  }
  .brand__name {
    font-family: "Cinzel", serif;
    font-weight: 400;
    font-size: 108px;
    line-height: 1;
    letter-spacing: 2px;
    color: var(--gold);
    white-space: nowrap;
  }
  .brand__tagline {
    margin-top: 14px;
    font-family: "Cormorant Garamond", serif;
    font-weight: 500;
    font-size: 40px;
    letter-spacing: 3px;
    color: var(--gold);
    text-transform: uppercase;
  }
  .contact {
    position: absolute;
    left: 0;
    right: 0;
    top: 740px;
    display: flex;
    align-items: center;
    justify-content: center;
    gap: 20px;
  }
  .contact__icon {
    width: 62px;
    height: 62px;
  }
  .contact__phone {
    font-family: "Montserrat", sans-serif;
    font-weight: 500;
    font-size: 46px;
    color: #ffffff;
    letter-spacing: 1px;
  }
</style>
</head>
<body>
  <main class="canvas">
    <section class="sticker">
      <div class="sticker__ring"></div>

      <div class="brand">
        <div class="brand__dot"></div>
        <h1 class="brand__name">FOLHA CLARA</h1>
        <p class="brand__tagline">Porque você é única</p>
      </div>

      <div class="contact">
        <svg class="contact__icon" viewBox="0 0 64 64" aria-hidden="true">
          <circle cx="32" cy="32" r="32" fill="var(--gold-light)"/>
          <path fill="#1f4749" d="M24.6 17.5c-1-.9-2.5-.9-3.4 0l-3 3c-1.6 1.6-2 4-1 6 4.2 8.6 11.2 15.6 19.8 19.8 2 1 4.4.6 6-1l3-3c.9-.9.9-2.4 0-3.4l-5-5c-.9-.9-2.4-.9-3.3 0l-2.4 2.4c-4.3-2.1-7.9-5.7-10-10l2.4-2.4c.9-.9.9-2.4 0-3.3z"/>
        </svg>
        <span class="contact__phone">(31) 9 5550-1820</span>
      </div>
    </section>
  </main>
</body>
</html>
```